Business Card Design

I need a business card for my company i am starting. I will be providing stump grinding services. I use a motorized machine to grind stumps down under the ground so that they are out of the way and out of sight. I'm looking for my card to have maroon or dark red somewhere in the card to match my truck. I'm going to use this card to advertise and also serve as a design to wrap my truck tailgate as advertisement so i want it to match. the dark maroon color of my truck. I wouldn't mind using bright colors or color for the rest of the card or the lettering or any designs on the card. In the images i have provided i like how there are saw blades integrated into these people advertisements. I also like the illustration of the stump grinder. I also provided a picture of the actual cutting wheel or blade of the grinder.

Industry/Entity Type

Business

Contact Information for Business Card

Company Name - Oakline Stump Grinding
Phone - 407-219-5573
Email - harlow.stumpwork@quillpost.net
Name and title - Thomas Harlow - Owner and operator
Company Slogan - You find them, I'll grind them

```html
<!DOCTYPE html>
<html lang="en">
<head>
<meta charset="utf-8">
<title>Oakline Stump Grinding – Business Card</title>
<link href="https://fonts.googleapis.com/css2?family=Open+Sans:wght@400;600&display=swap" rel="stylesheet">
<style>
  :root {
    --page-bg: #e9e6e2;
    --card-white: #ffffff;
    --maroon: #2c1112;
    --band-grey: #4b4b4d;
    --ink: #1c1c1c;
    --light-text: #ffffff;
    --saw-orange: #f08a24;
  }
  * { margin: 0; padding: 0; box-sizing: border-box; }
  html, body {
    width: 1189px;
    height: 1200px;
    overflow: hidden;
    background: var(--page-bg);
    font-family: "Open Sans", sans-serif;
  }
  .business-card {
    position: absolute;
    left: 32px;
    top: 279px;
    width: 1125px;
    height: 642px;
    background: var(--card-white);
    overflow: hidden;
    box-shadow: 0 6px 18px rgba(0,0,0,0.18);
  }
  .wave-art {
    position: absolute;
    inset: 0;
    width: 100%;
    height: 100%;
  }
  .brand {
    position: absolute;
    left: 118px;
    top: 70px;
    display: flex;
    align-items: center;
    gap: 22px;
  }
  .brand-dot {
    width: 120px;
    height: 120px;
    border-radius: 50%;
    background: var(--saw-orange);
    flex: none;
  }
  .brand-name {
    font-weight: 600;
    font-size: 54px;
    line-height: 1.08;
    color: var(--maroon);
  }
  .slogan {
    position: absolute;
    left: 53px;
    top: 268px;
    font-size: 34px;
    font-weight: 400;
    color: var(--ink);
    letter-spacing: 0.3px;
  }
  .contact-block {
    position: absolute;
    right: 72px;
    top: 358px;
    text-align: right;
    color: var(--light-text);
  }
  .person-name {
    font-weight: 600;
    font-size: 45px;
    line-height: 1.15;
  }
  .person-title {
    font-size: 32px;
    line-height: 1.1;
    margin-bottom: 34px;
  }
  .contact-line {
    display: flex;
    justify-content: flex-end;
    align-items: center;
    gap: 14px;
    font-size: 32px;
    line-height: 42px;
  }
  .contact-icon {
    width: 26px;
    height: 26px;
    flex: none;
  }
</style>
</head>
<body>
  <main class="business-card">
    <svg class="wave-art" viewBox="0 0 1125 642" preserveAspectRatio="none" aria-hidden="true">
      <path fill="var(--band-grey)"
        d="M0,470 C200,440 430,400 620,290 C790,190 950,150 1125,150 L1125,160 C950,160 800,210 650,310 C450,440 200,482 0,530 Z"/>
      <path fill="var(--maroon)"
        d="M0,542 C200,492 460,455 662,322 C812,222 962,172 1125,168 L1125,642 L0,642 Z"/>
    </svg>

    <div class="brand">
      <span class="brand-dot"></span>
      <div class="brand-name">Oakline<br>Stump Grinding</div>
    </div>

    <p class="slogan">You find them, I'll grind them</p>

    <section class="contact-block">
      <h1 class="person-name">Thomas Harlow</h1>
      <p class="person-title">Owner and operator</p>
      <p class="contact-line">
        <span>407-219-5573</span>
        <svg class="contact-icon" viewBox="0 0 24 24" aria-hidden="true">
          <rect width="24" height="24" fill="#fff"/>
          <path fill="var(--maroon)" d="M7 4 L10 4 L11 8 L9 10 C10 13 11 14 14 15 L16 13 L20 14 L20 17 C20 19 18 20 16 20 C10 19 5 14 4 8 C4 6 5 4 7 4 Z"/>
        </svg>
      </p>
      <p class="contact-line">
        <span>harlow.stumpwork@quillpost.net</span>
        <svg class="contact-icon" viewBox="0 0 24 24" aria-hidden="true">
          <rect width="24" height="24" fill="#fff"/>
          <rect x="4" y="6" width="16" height="12" fill="none" stroke="var(--maroon)" stroke-width="1.8"/>
          <path d="M4 6 L12 13 L20 6" fill="none" stroke="var(--maroon)" stroke-width="1.8"/>
        </svg>
      </p>
    </section>
  </main>
</body>
</html>
```